Letterhead

Can you please design me a letterhead that I can use electronically in word as a template. I have attached my business card as I would like the design to reflect this logo.

```html
<!DOCTYPE html>
<html lang="en">
<head>
<meta charset="utf-8">
<title>Meridale Business Consultants – Letterhead</title>
<link rel="stylesheet" href="https://fonts.googleapis.com/css2?family=Open+Sans:wght@400;600;700&family=Arimo:wght@400&display=swap">
<style>
  :root {
    --brand-red: #c0272d;
    --brand-red-deep: #9e1c22;
    --brand-red-light: #d3544f;
    --charcoal: #2e2e2e;
    --charcoal-light: #555555;
    --text-grey: #4a4a4a;
    --text-dark: #222222;
    --paper: #ffffff;
  }
  * { box-sizing: border-box; margin: 0; padding: 0; }
  html, body { width: 848px; height: 1200px; overflow: hidden; background: var(--paper); }
  .letterhead {
    position: relative;
    width: 848px;
    height: 1200px;
    background: var(--paper);
    font-family: "Open Sans", Arial, sans-serif;
    overflow: hidden;
  }
  .brand {
    position: absolute;
    left: 24px;
    top: 14px;
  }
  .brand-name {
    font-family: "Open Sans", Arial, sans-serif;
    font-weight: 400;
    font-size: 58px;
    line-height: 1;
    color: var(--brand-red);
    letter-spacing: 0.5px;
  }
  .brand-tagline {
    margin-top: 6px;
    margin-left: 5px;
    font-family: "Arimo", Arial, sans-serif;
    font-size: 14.5px;
    color: var(--text-dark);
  }
  .corner-accent, .footer-band {
    position: absolute;
    left: 0;
    top: 0;
  }
  .contact {
    position: absolute;
    left: 16px;
    top: 950px;
    color: var(--text-grey);
  }
  .contact-name {
    font-size: 19px;
    font-weight: 700;
    color: var(--text-grey);
  }
  .contact-name .divider {
    font-weight: 400;
    margin: 0 6px 0 6px;
    color: var(--text-grey);
  }
  .contact-name .role {
    font-weight: 400;
    color: var(--brand-red);
  }
  .contact-line {
    font-size: 13px;
    margin-top: 14px;
    color: var(--text-dark);
  }
  .contact-line:first-of-type { margin-top: 18px; }
  .contact-line .label { color: var(--brand-red); }
</style>
</head>
<body>
<div class="letterhead">

  <svg class="corner-accent" width="848" height="1200" viewBox="0 0 848 1200" role="img" aria-label="Dark charcoal mosaic of squares in the top right corner">
    <defs>
      <linearGradient id="charcoalFade" x1="0" y1="0" x2="1" y2="1">
        <stop offset="0" stop-color="#3c3c3c"/>
        <stop offset="0.5" stop-color="#2a2a2a"/>
        <stop offset="1" stop-color="#4a4a4a"/>
      </linearGradient>
    </defs>
    <polygon points="615,0 848,0 848,471" fill="url(#charcoalFade)"/>
  </svg>

  <svg class="footer-band" width="848" height="1200" viewBox="0 0 848 1200" role="img" aria-label="Red mosaic of squares forming a slanted band along the bottom">
    <defs>
      <linearGradient id="redBand" x1="0" y1="0" x2="1" y2="0.3">
        <stop offset="0" stop-color="var(--brand-red-light)"/>
        <stop offset="0.5" stop-color="var(--brand-red)"/>
        <stop offset="1" stop-color="var(--brand-red-deep)"/>
      </linearGradient>
    </defs>
    <polygon points="0,1111 848,980 848,1200 0,1200" fill="url(#redBand)"/>
  </svg>

  <header class="brand">
    <div class="brand-name">meridale</div>
    <div class="brand-tagline">Business Consultants Pty Ltd</div>
  </header>

  <footer class="contact">
    <div class="contact-name">Helena Marsh<span class="divider">|</span><span class="role">Principal</span></div>
    <p class="contact-line"><span class="label">P</span> : 0400 555 182</p>
    <p class="contact-line"><span class="label">E</span> : helena@meridale.net.au</p>
    <p class="contact-line"><span class="label">ACN</span> : 000 123 456</p>
  </footer>

</div>
</body>
</html>
```